Business Card & Full Stationary design For Summit Quarry
Summit Quarry For Marble & Granite
Business Card & Full Stationary design For Summit Quarry  - Construction
Creative Brief
Professional
Eng. Karim Haddouri
C.E.O
14 Shari' Nakhil el Wadi, Rawdatein, Giza, 12487, Egypt
kbh@summitquarry.com.eg
www.summitquarry.com.eg
we need everything to be included in the design ( CD, CD Cover, Letterhead, Envelopes, portfolio cover, etc..)
q7rimo q7rimo
I would highly appreciate if you can provide your concepts showing all the required stationaries including the back side of the B.Card ( Letterhead, 2 size envelope, Portfolio cover, CD, CD cover, Backgrounds for smartphones and Computers .)
Vonto Vonto

```html
<!DOCTYPE html>
<html lang="en">
<head>
<meta charset="utf-8">
<title>Summit Quarry – Business Card</title>
<link rel="stylesheet" href="https://fonts.googleapis.com/css2?family=Open+Sans:wght@300;400;600;700&display=swap">
<style>
  :root {
    --backdrop: #e4e4e4;
    --card: #ffffff;
    --sand: #c9bb9f;
    --stone: #6e6967;
    --ink: #3a3838;
    --paper-text: #ffffff;
  }
  * { margin: 0; padding: 0; box-sizing: border-box; }
  html, body {
    width: 1200px; height: 883px; overflow: hidden;
    background: var(--backdrop);
    font-family: "Open Sans", Arial, sans-serif;
  }
  .canvas { position: relative; width: 1200px; height: 883px; }
  .card {
    position: absolute; left: 260px;
    width: 680px; height: 390px;
    background: var(--card);
    border-radius: 34px;
    overflow: hidden;
    box-shadow: 0 6px 18px rgba(0,0,0,0.12);
  }
  .card--brand { top: 40px; }
  .card--contact { top: 455px; }

  /* Brand side */
  .brand-band {
    position: absolute; top: 92px; left: 400px; right: 0; height: 60px;
    display: flex;
  }
  .brand-band__web {
    flex: 0 0 196px; background: var(--sand);
    color: var(--ink); font-size: 11px; letter-spacing: .3px;
    display: flex; align-items: center; justify-content: center;
    white-space: nowrap;
  }
  .brand-band__block { flex: 1; background: var(--stone); }
  .brand-mark {
    position: absolute; left: 150px; top: 172px; width: 280px;
    text-align: center; color: var(--sand);
  }
  .brand-mark__name {
    font-size: 40px; font-weight: 300; letter-spacing: 2px; line-height: 1.05;
  }
  .brand-mark__tagline {
    margin-top: 8px; font-size: 11px; font-weight: 300; letter-spacing: 2px;
  }

  /* Contact side */
  .person { position: absolute; left: 96px; top: 46px; color: var(--ink); }
  .person__name { font-size: 30px; font-weight: 400; letter-spacing: .5px; line-height: 1.1; }
  .person__name strong { font-weight: 700; }
  .person__role { font-size: 12px; font-weight: 700; letter-spacing: .5px; margin-top: 2px; }
  .panel-phone {
    position: absolute; left: 0; top: 158px; width: 286px; height: 100px;
    background: var(--stone); color: var(--paper-text);
    padding: 14px 0 0 96px; font-size: 15px; line-height: 1.3;
  }
  .panel-web {
    position: absolute; left: 286px; right: 0; top: 110px; height: 148px;
    background: var(--sand); color: var(--paper-text);
    padding: 46px 0 0 50px; font-size: 15px; line-height: 1.3;
  }
  .panel__label { font-weight: 600; letter-spacing: .5px; }
  .address {
    position: absolute; left: 0; right: 0; top: 284px;
    text-align: center; color: var(--ink);
    font-size: 13px; letter-spacing: .5px; line-height: 1.45;
    padding-left: 40px;
  }
  .address strong { font-weight: 700; }
</style>
</head>
<body>
<main class="canvas">
  <section class="card card--brand" aria-label="Business card, brand side">
    <div class="brand-band">
      <div class="brand-band__web">www.summitquarry.com.eg</div>
      <div class="brand-band__block"></div>
    </div>
    <div class="brand-mark">
      <div class="brand-mark__name">Summit<br>Quarry</div>
      <div class="brand-mark__tagline">MARBLE &amp; GRANITE</div>
    </div>
  </section>

  <section class="card card--contact" aria-label="Business card, contact side">
    <div class="person">
      <div class="person__name">SAMIR <strong>ALDANA</strong></div>
      <div class="person__role">SENIOR GRAPHIC DESIGNER</div>
    </div>
    <div class="panel-web">
      <div class="panel__label">EMAIL &amp; WEB</div>
      <div>INFO@SUMMITQUARRY.COM.EG</div>
      <div>WWW.SUMMITQUARRY.COM.EG</div>
    </div>
    <div class="panel-phone">
      <div class="panel__label">PHONE &amp; FAX</div>
      <div>+20 2 3571 4826</div>
      <div>+20 100 482 6153</div>
    </div>
    <div class="address">
      <div>14 SHARI' NAKHIL EL WADI, <strong>GIZA</strong> 12487</div>
      <div><strong>EGYPT</strong></div>
    </div>
  </section>
</main>
</body>
</html>
```